RW Skyline Imaging Web Site design

I am looking for a responsive single page website deign for rwskylineimages.example. This is a drone based aerial photography and cinematography business. It should have an about us section, a services section that contains photograph service, Video footage, and Aerial mapping all under the services section, a pricing section, and then a contact page for customers to contact us.

Coding

Coded - Design and coding required

Number of Pages Required

1 page

Font styles to use
Sans Serif

Colors

Designer to choose colors to be used in the design.

Requirements
Must have
• Responsive design. About us section, services section, pricing section under the services links, and contact us section, that links to a submission page where they can send Name, address, email, and comments on what they are interested in.
• See flyquad7x.example - looking for similar design.
Should not have
• clutter, or too busy design

```html
<!DOCTYPE html>
<html lang="en">
<head>
<meta charset="utf-8">
<title>RW Skyline Imaging</title>
<link rel="stylesheet" href="https://fonts.googleapis.com/css2?family=Lato:wght@400;700;900&display=swap">
<style>
:root{
  --orange:#f28a1e;
  --dark:#1f2326;
  --text:#2b2b2b;
  --muted:#666;
  --grey:#7a7a7a;
  --line:#d8d8d8;
  --white:#fff;
}
*{box-sizing:border-box;margin:0;padding:0}
html,body{width:1200px;height:3180px;overflow:hidden}
body{font-family:'Lato',sans-serif;color:var(--text);background:var(--white);position:relative}
.abs{position:absolute}

/* hero */
.hero{position:absolute;left:0;top:0;width:1200px;height:572px;
  background:linear-gradient(180deg,#2a3034 0%,#3b4634 22%,#5a6a3a 45%,#4e5a33 70%,#6b6350 100%)}
.hero-shade{position:absolute;inset:0;background:linear-gradient(180deg,rgba(0,0,0,.55) 0%,rgba(0,0,0,.15) 30%,rgba(0,0,0,.1) 100%)}
.brand{position:absolute;left:98px;top:50px;display:flex;align-items:center;gap:12px;color:var(--white);font-size:19px;letter-spacing:3px;font-weight:400}
.brand .dot{width:22px;height:22px;border-radius:50%;background:var(--orange)}
.nav{position:absolute;top:58px;left:518px;display:flex;gap:0;font-size:15px;font-weight:700;color:var(--white)}
.nav a{color:inherit;text-decoration:none;margin-right:46px}
.nav a.active{color:var(--orange)}
.nav svg{margin-top:1px}
.hero h1{position:absolute;top:192px;width:100%;text-align:center;color:var(--white);font-size:51px;font-weight:700;letter-spacing:.5px}
.hero p{position:absolute;top:266px;width:100%;text-align:center;color:var(--white);font-size:22px}
.hero .btn-ghost{position:absolute;left:512px;top:329px;width:177px;height:46px;border:2px solid var(--white);color:var(--white);font-size:15px;font-weight:700;display:flex;align-items:center;justify-content:center}
.dots{position:absolute;top:499px;left:569px;display:flex;gap:4px}
.dots span{width:11px;height:11px;border-radius:50%;border:1.5px solid var(--white)}
.dots span.on{background:var(--white)}

/* welcome */
.welcome h2{position:absolute;left:98px;top:664px;font-size:32px;font-weight:700;line-height:42px;color:#111}
.welcome p{position:absolute;left:98px;width:465px;font-size:14px;line-height:26px;color:var(--muted)}
.btn-outline{position:absolute;border:2px solid #cfcfcf;color:var(--orange);font-weight:700;font-size:14px;display:flex;align-items:center;justify-content:center}
.video{position:absolute;left:615px;top:674px;width:487px;height:317px;border:1px solid var(--line);padding:4px;background:var(--white)}
.video .media{width:100%;height:100%;background:linear-gradient(180deg,#4f7a3a 0%,#6c8f4a 45%,#8fa665 75%,#7f9658 100%);position:relative}
.video .play{position:absolute;left:210px;top:120px}

/* services */
.services{position:absolute;left:0;top:1071px;width:1200px;height:610px;
  background:linear-gradient(180deg,#b89a7c 0%,#6d6e72 25%,#3f4a58 60%,#34404c 100%)}
.section-title{position:absolute;width:100%;text-align:center;font-size:32px;font-weight:700}
.services .section-title{color:var(--white);top:68px}
.svc{position:absolute;top:144px;width:312px;height:390px;background:var(--white)}
.svc .media{height:180px}
.svc .icon{position:absolute;left:126px;top:152px;width:60px;height:60px;border-radius:50%;background:var(--orange);border:3px solid var(--white);display:flex;align-items:center;justify-content:center}
.svc h3{position:absolute;top:226px;width:100%;text-align:center;font-size:21px;font-weight:700;color:#111}
.svc p{position:absolute;top:262px;left:30px;right:30px;text-align:center;font-size:14px;line-height:23px;color:var(--muted)}
.svc .more{position:absolute;top:340px;width:100%;text-align:center;color:var(--orange);font-weight:700;font-size:14px}

/* pricing */
.pricing .section-title{top:1760px;color:#111}
.plan{position:absolute;top:1855px;height:396px;background:var(--white);border:1px solid var(--line)}
.plan.featured{top:1845px;height:418px;box-shadow:0 0 8px rgba(0,0,0,.25);border:none}
.plan h4{text-align:center;font-size:20px;font-weight:700;color:#222;margin-top:20px;height:50px;line-height:30px}
.plan.featured h4{margin-top:18px;height:56px}
.plan .price{height:48px;background:var(--grey);color:var(--white);display:flex;align-items:baseline;justify-content:center;padding-top:6px;font-size:28px;font-weight:700}
.plan.featured .price{background:var(--orange)}
.plan .price small{font-size:13px;font-weight:400;margin-left:3px}
.plan ul{list-style:none;margin:24px 0 0 22px}
.plan li{display:flex;align-items:center;gap:14px;font-size:14px;color:#555;height:32px}
.plan .sign{position:absolute;left:50%;transform:translateX(-50%);bottom:32px;width:106px;height:42px;border:2px solid #cfcfcf;color:var(--orange);font-weight:700;font-size:16px;display:flex;align-items:center;justify-content:center}
.plan.featured .sign{background:var(--orange);color:var(--white);border-color:var(--orange);bottom:40px}

/* contact */
.contact{position:absolute;left:0;top:2347px;width:1200px;height:464px;
  background:linear-gradient(160deg,#2e3a2b 0%,#3d4a35 40%,#34422f 70%,#2c3a3c 100%)}
.contact .section-title{color:var(--white);top:62px}
.field{position:absolute;background:var(--white);font-size:14px;color:#444;padding:11px 14px}
.btn-solid{position:absolute;background:var(--orange);color:var(--white);font-weight:700;font-size:16px;display:flex;align-items:center;justify-content:center}

/* footer */
.footer h5{position:absolute;top:2882px;font-size:17px;font-weight:700;color:#111}
.footer .brand-foot{position:absolute;left:98px;top:2980px;display:flex;align-items:center;gap:10px;font-size:16px;letter-spacing:3px;color:#111}
.footer .brand-foot .dot{width:18px;height:18px;border-radius:50%;background:var(--orange)}
.links{position:absolute;left:414px;top:2924px;list-style:none;font-size:12px;color:#444;line-height:25px}
.newsletter p{position:absolute;left:586px;top:2930px;width:260px;font-size:12px;line-height:20px;color:#444}
.newsletter .email{position:absolute;left:586px;top:2988px;width:254px;height:30px;border-bottom:1px solid var(--line);font-size:11px;color:#888;padding:6px 14px}
.contact-list{position:absolute;left:898px;top:2938px;list-style:none;font-size:12px;color:#444}
.contact-list li{display:flex;gap:18px;margin-bottom:16px;line-height:16px}
.contact-list svg{flex:none;margin-top:1px}
.footer hr{position:absolute;left:98px;top:3099px;width:1004px;border:none;border-top:1px solid var(--line)}
.copy{position:absolute;left:98px;top:3128px;font-size:12px;color:#444}
.social{position:absolute;left:976px;top:3122px;display:flex;gap:6px}
.social span{width:26px;height:26px;border-radius:50%;border:1.5px solid var(--orange)}
</style>
</head>
<body>

<header class="hero" role="img" aria-label="Aerial photo of a green countryside village with fields and houses">
  <div class="hero-shade"></div>
</header>
<div class="brand"><span class="dot"></span>RW Skyline Imaging</div>
<nav class="nav">
  <a class="active">HOME</a><a>ABOUT US</a><a>SERVICES</a><a>PRICING</a><a>CONTACT</a>
  <svg width="16" height="16" viewBox="0 0 16 16"><circle cx="6.5" cy="6.5" r="5" fill="none" stroke="#fff" stroke-width="2.2"/><line x1="10" y1="10" x2="14.5" y2="14.5" stroke="#fff" stroke-width="2.4"/></svg>
</nav>
<section class="hero-copy">
  <h1 class="abs" style="top:192px;width:100%;text-align:center;color:#fff;font-size:51px;font-weight:700">RW SKYLINE IMAGING</h1>
  <p class="abs" style="top:266px;width:100%;text-align:center;color:#fff;font-size:22px">We are into drone based aerial photography and cinematography business</p>
  <div class="abs" style="left:512px;top:329px;width:177px;height:46px;border:2px solid #fff;color:#fff;font-size:15px;font-weight:700;display:flex;align-items:center;justify-content:center">GET MORE INFO</div>
  <div class="dots"><span class="on"></span><span></span><span></span><span></span></div>
</section>

<section class="welcome">
  <h2>WELCOME TO<br>RW SKYLINE IMAGING</h2>
  <p style="top:764px">At vero eos et accusamus et iusto odio dignissimos ducimus qui blanditi ispr aesentium voluptatum deleniti atque corr.</p>
  <p style="top:842px">Rupti quos dolores et quas molestias excepturi sint occaecati cupiditate non provident, similique sunt in culpa qui officia deserunt mollitia animi, id est laborum et dolorum um quidem.</p>
  <div class="btn-outline" style="left:98px;top:956px;width:118px;height:38px">READ MORE</div>
  <div class="video">
    <div class="media" role="img" aria-label="Video still of a drone pilot flying a white quadcopter in a park">
      <svg class="play" width="58" height="58" viewBox="0 0 58 58"><circle cx="29" cy="29" r="27" fill="#222" stroke="#fff" stroke-width="3"/><path d="M23 17 L41 29 L23 41 Z" fill="#fff"/></svg>
    </div>
  </div>
</section>

<section class="services" role="img" aria-label="Background aerial view of a city at dusk">
  <h2 class="section-title">OUR SERVICES</h2>
  <article class="svc" style="left:98px">
    <div class="media" role="img" aria-label="Aerial photo of a golf course by a lake" style="background:linear-gradient(180deg,#6f8f56,#4d7a3c 60%,#3d6e7a)"></div>
    <div class="icon"><svg width="28" height="24" viewBox="0 0 28 24"><rect x="2" y="2" width="24" height="20" fill="none" stroke="#fff" stroke-width="2.4"/><path d="M5 19 L11 11 L15 16 L19 12 L23 19 Z" fill="#fff"/><circle cx="19" cy="7" r="2" fill="#fff"/></svg></div>
    <h3>Photograph Service</h3>
    <p>Lorem ipsum dolor sit amet, cons ectetur adipiscing elit, sed do eiusmod tempor incididunt ut labore et</p>
    <div class="more">READ MORE</div>
  </article>
  <article class="svc" style="left:444px">
    <div class="media" role="img" aria-label="Drone in flight above a remote controller" style="background:linear-gradient(180deg,#9aa3ab,#c4c8cb 50%,#6b6d70)"></div>
    <div class="icon"><svg width="30" height="22" viewBox="0 0 30 22"><rect x="1" y="3" width="19" height="16" rx="2" fill="#fff"/><path d="M21 9 L29 3 V19 L21 13 Z" fill="#fff"/></svg></div>
    <h3>Video Footage</h3>
    <p>Lorem ipsum dolor sit amet, cons ectetur adipiscing elit, sed do eiusmod tempor incididunt ut labore et</p>
    <div class="more">READ MORE</div>
  </article>
  <article class="svc" style="left:788px">
    <div class="media" role="img" aria-label="Satellite style aerial map of a city and river" style="background:linear-gradient(160deg,#5a6f5a,#7a8a80 45%,#4e6a78)"></div>
    <div class="icon"><svg width="22" height="28" viewBox="0 0 22 28"><path d="M11 1 C5 1 1 5.5 1 11 C1 18 11 27 11 27 C11 27 21 18 21 11 C21 5.5 17 1 11 1 Z" fill="#fff"/><circle cx="11" cy="11" r="4" fill="#f28a1e"/></svg></div>
    <h3>Aerial mapping</h3>
    <p>Lorem ipsum dolor sit amet, cons ectetur adipiscing elit, sed do eiusmod tempor incididunt ut labore et</p>
    <div class="more">READ MORE</div>
  </article>
</section>

<section class="pricing">
  <h2 class="section-title">PRICING PLAN</h2>
  <div class="plan" style="left:98px;width:237px"><h4>BASIC</h4><div class="price">$3.28<small>/month</small></div>
    <ul><li><svg width="14" height="14"><circle cx="7" cy="7" r="7" fill="#555"/><path d="M3.5 7 L6 9.5 L10.5 4.5" stroke="#fff" stroke-width="1.8" fill="none"/></svg>Free Domain Name</li><li><svg width="14" height="14"><circle cx="7" cy="7" r="7" fill="#555"/><path d="M3.5 7 L6 9.5 L10.5 4.5" stroke="#fff" stroke-width="1.8" fill="none"/></svg>Sed ut perspiciatis unde</li><li><svg width="14" height="14"><circle cx="7" cy="7" r="7" fill="#555"/><path d="M3.5 7 L6 9.5 L10.5 4.5" stroke="#fff" stroke-width="1.8" fill="none"/></svg>Nemo enim ipsam volupt</li><li><svg width="14" height="14"><circle cx="7" cy="7" r="7" fill="#555"/><path d="M3.5 7 L6 9.5 L10.5 4.5" stroke="#fff" stroke-width="1.8" fill="none"/></svg>Ut enim ad minimav</li><li><svg width="14" height="14"><circle cx="7" cy="7" r="7" fill="#555"/><path d="M3.5 7 L6 9.5 L10.5 4.5" stroke="#fff" stroke-width="1.8" fill="none"/></svg>Sed ut perspiciatis</li></ul>
    <div class="sign">SIGN UP</div></div>
  <div class="plan featured" style="left:348px;width:250px"><h4>STANDARD</h4><div class="price">$14.17<small>/month</small></div>
    <ul><li><svg width="14" height="14"><circle cx="7" cy="7" r="7" fill="#f28a1e"/><path d="M3.5 7 L6 9.5 L10.5 4.5" stroke="#fff" stroke-width="1.8" fill="none"/></svg>Free Domain Name</li><li><svg width="14" height="14"><circle cx="7" cy="7" r="7" fill="#f28a1e"/><path d="M3.5 7 L6 9.5 L10.5 4.5" stroke="#fff" stroke-width="1.8" fill="none"/></svg>Sed ut perspiciatis unde</li><li><svg width="14" height="14"><circle cx="7" cy="7" r="7" fill="#f28a1e"/><path d="M3.5 7 L6 9.5 L10.5 4.5" stroke="#fff" stroke-width="1.8" fill="none"/></svg>Nemo enim ipsam volupt</li><li><svg width="14" height="14"><circle cx="7" cy="7" r="7" fill="#f28a1e"/><path d="M3.5 7 L6 9.5 L10.5 4.5" stroke="#fff" stroke-width="1.8" fill="none"/></svg>Ut enim ad minimav</li><li><svg width="14" height="14"><circle cx="7" cy="7" r="7" fill="#f28a1e"/><path d="M3.5 7 L6 9.5 L10.5 4.5" stroke="#fff" stroke-width="1.8" fill="none"/></svg>Sed ut perspiciatis</li></ul>
    <div class="sign">SIGN UP</div></div>
  <div class="plan" style="left:611px;width:235px"><h4>PRO</h4><div class="price">$17.45<small>/month</small></div>
    <ul><li><svg width="14" height="14"><circle cx="7" cy="7" r="7" fill="#555"/><path d="M3.5 7 L6 9.5 L10.5 4.5" stroke="#fff" stroke-width="1.8" fill="none"/></svg>Free Domain Name</li><li><svg width="14" height="14"><circle cx="7" cy="7" r="7" fill="#555"/><path d="M3.5 7 L6 9.5 L10.5 4.5" stroke="#fff" stroke-width="1.8" fill="none"/></svg>Sed ut perspiciatis unde</li><li><svg width="14" height="14"><circle cx="7" cy="7" r="7" fill="#555"/><path d="M3.5 7 L6 9.5 L10.5 4.5" stroke="#fff" stroke-width="1.8" fill="none"/></svg>Nemo enim ipsam volupt</li><li><svg width="14" height="14"><circle cx="7" cy="7" r="7" fill="#555"/><path d="M3.5 7 L6 9.5 L10.5 4.5" stroke="#fff" stroke-width="1.8" fill="none"/></svg>Ut enim ad minimav</li><li><svg width="14" height="14"><circle cx="7" cy="7" r="7" fill="#555"/><path d="M3.5 7 L6 9.5 L10.5 4.5" stroke="#fff" stroke-width="1.8" fill="none"/></svg>Sed ut perspiciatis</li></ul>
    <div class="sign">SIGN UP</div></div>
  <div class="plan" style="left:863px;width:238px"><h4>BUSINESS</h4><div class="price">$90.30<small>/month</small></div>
    <ul><li><svg width="14" height="14"><circle cx="7" cy="7" r="7" fill="#555"/><path d="M3.5 7 L6 9.5 L10.5 4.5" stroke="#fff" stroke-width="1.8" fill="none"/></svg>Free Domain Name</li><li><svg width="14" height="14"><circle cx="7" cy="7" r="7" fill="#555"/><path d="M3.5 7 L6 9.5 L10.5 4.5" stroke="#fff" stroke-width="1.8" fill="none"/></svg>Sed ut perspiciatis unde</li><li><svg width="14" height="14"><circle cx="7" cy="7" r="7" fill="#555"/><path d="M3.5 7 L6 9.5 L10.5 4.5" stroke="#fff" stroke-width="1.8" fill="none"/></svg>Nemo enim ipsam volupt</li><li><svg width="14" height="14"><circle cx="7" cy="7" r="7" fill="#555"/><path d="M3.5 7 L6 9.5 L10.5 4.5" stroke="#fff" stroke-width="1.8" fill="none"/></svg>Ut enim ad minimav</li><li><svg width="14" height="14"><circle cx="7" cy="7" r="7" fill="#555"/><path d="M3.5 7 L6 9.5 L10.5 4.5" stroke="#fff" stroke-width="1.8" fill="none"/></svg>Sed ut perspiciatis</li></ul>
    <div class="sign">SIGN UP</div></div>
</section>

<section class="contact" role="img" aria-label="Background aerial view of a housing estate beside water">
  <h2 class="section-title">GET IN TOUCH</h2>
  <div class="field" style="left:259px;top:133px;width:335px;height:42px">First Name</div>
  <div class="field" style="left:608px;top:133px;width:333px;height:42px">Last Name</div>
  <div class="field" style="left:259px;top:186px;width:335px;height:43px">Email</div>
  <div class="field" style="left:608px;top:186px;width:333px;height:43px">Address</div>
  <div class="field" style="left:259px;top:242px;width:682px;height:80px">Comments</div>
  <div class="btn-solid" style="left:532px;top:350px;width:136px;height:44px">CONTACT US</div>
</section>

<footer class="footer">
  <div class="brand-foot"><span class="dot"></span>RW Skyline Imaging</div>
  <h5 style="left:414px">QUICK LINKS</h5>
  <ul class="links"><li>Help</li><li>FAQ</li><li>Support</li><li>Sitemap</li><li>Terms Of Use</li><li>Privacy Statement</li></ul>
  <h5 style="left:586px">NEWSLETTER SUBSCRIPTION</h5>
  <div class="newsletter">
    <p>Register your Email Address to get Information about us</p>
    <div class="email">Email Address</div>
    <div class="btn-solid" style="left:586px;top:3036px;width:96px;height:30px;font-size:11px">SUBSCRIBE</div>
  </div>
  <h5 style="left:898px">CONTACT US</h5>
  <ul class="contact-list">
    <li><svg width="12" height="15" viewBox="0 0 12 15"><path d="M6 0 C2.7 0 0 2.6 0 5.8 C0 10 6 15 6 15 C6 15 12 10 12 5.8 C12 2.6 9.3 0 6 0 Z" fill="#f28a1e"/><circle cx="6" cy="5.8" r="2.2" fill="#fff"/></svg><span>Level 12, 48 Harbour Lane<br>Bristol, UK</span></li>
    <li><svg width="13" height="13" viewBox="0 0 13 13"><path d="M2 0 L5 3 L3.5 5 C4.5 7 6 8.5 8 9.5 L10 8 L13 11 L11 13 C5 12 1 8 0 2 Z" fill="#f28a1e"/></svg><span>1 555 010 2040</span></li>
    <li><svg width="14" height="13" viewBox="0 0 14 13"><rect x="3" y="0" width="8" height="4" fill="#f28a1e"/><rect x="0" y="4" width="14" height="6" rx="1" fill="#f28a1e"/><rect x="3" y="8" width="8" height="5" fill="#f28a1e" stroke="#fff" stroke-width="1"/></svg><span>1 555 010 3050</span></li>
    <li><svg width="14" height="11" viewBox="0 0 14 11"><rect width="14" height="11" rx="1" fill="#f28a1e"/><path d="M0.5 1 L7 6 L13.5 1" stroke="#fff" stroke-width="1.3" fill="none"/></svg><span>info@rwskylineimages.example</span></li>
  </ul>
  <hr>
  <div class="copy">Copyrights © 2017, RW Skyline Imaging. All rights reserved.</div>
  <div class="social"><span></span><span></span><span></span><span></span></div>
</footer>

</body>
</html>
```